New Record Label needs a Web design

We are Iron Heron: a London based, new & independent music production company aimed at the 25-40 age group. The musical style is Soul/Classic Brelvane.
We have at the moment just one signed artist, but will expand in the future.
We dont' have any webpage yet and are looking for an innovative web design for our webpage www.iron-heron-example.com
I have uploaded our company logo.

Initially the whole website will only have 3 tabs: Home page/Artists/Contact

The design should be classic and high-end, but can be a bit crazy too.

```html
<!DOCTYPE html>
<html lang="en">
<head>
<meta charset="utf-8">
<title>Iron Heron — Soul &amp; Classic Brelvane</title>
<link rel="stylesheet" href="https://fonts.googleapis.com/css2?family=Open+Sans:wght@400;600;700&display=swap">
<style>
:root{
  --ink:#1e1e1e;
  --ink-deep:#000;
  --panel:#4a4a4a;
  --footer:#1c1c1c;
  --red:#e8373a;
  --orange:#f0652f;
  --white:#fff;
  --text:#3a3a3a;
  --muted:#bdbdbd;
  --line:#3a3a3a;
}
*{box-sizing:border-box;margin:0;padding:0}
html,body{width:845px;height:1200px;overflow:hidden;background:var(--white)}
body{position:relative;font-family:"Open Sans",Arial,sans-serif;color:var(--text)}
.abs{position:absolute}
.center{text-align:center}

/* header */
.site-header{left:12px;top:14px;width:818px;height:69px;background:var(--ink);border-bottom:2px solid var(--red)}
.brand{left:128px;top:20px;display:flex;align-items:center;gap:10px}
.brand-mark{width:30px;height:30px;border-radius:50%;background:var(--red)}
.brand-name{color:var(--red);font-size:24px;font-weight:600;letter-spacing:.5px}
.nav{left:452px;top:0;height:67px;display:flex}
.nav a{display:flex;align-items:center;gap:6px;padding:0 18px;color:var(--white);font-size:10px;text-decoration:none;border-left:1px solid #262626;height:67px}
.nav a.active{background:#0d0d0d;font-weight:700}
.nav svg{width:12px;height:12px;fill:var(--white)}
.nav a.active svg{fill:var(--red)}

/* hero */
.hero{left:12px;top:83px;width:818px;height:235px;background:linear-gradient(120deg,#3b2a1c 0%,#7a5a3c 35%,#b08a5e 55%,#d8c3a2 80%,#c9b08b 100%)}
.hero-title{left:0;top:123px;width:818px;color:var(--white);font-size:23px;font-weight:700;text-shadow:0 2px 4px rgba(0,0,0,.7);letter-spacing:.3px}
.hero-arrow{top:98px;width:26px;height:22px;fill:var(--white)}
.hero-dots{left:391px;top:218px;display:flex;gap:4px}
.hero-dots span{width:10px;height:10px;border-radius:50%;border:1.5px solid var(--white)}
.hero-dots span.on{background:var(--red)}

/* player */
.player-band{left:12px;top:320px;width:818px;height:74px;background:var(--panel)}
.player-title{left:0;top:11px;width:818px;color:var(--white);font-size:14.5px;font-weight:700}
.player-btns{left:136px;top:40px;display:flex;gap:5px;align-items:center}
.player-bar{left:211px;top:40px;width:466px;height:22px;background:var(--white);border-radius:2px;font-size:7px;color:#999}
.volume{left:335px;top:0;width:93px;height:22px;background:#e6e6e6}

/* intro */
.intro-title{left:0;top:409px;width:845px;font-size:18px;font-weight:700;color:#444}
.intro-title em{font-style:normal;color:var(--red)}
.intro-copy{left:139px;top:439px;width:567px;font-size:11.2px;line-height:18.2px;color:#444}
.intro-copy p+p{margin-top:18px}

/* artists */
.artists{left:12px;top:620px;width:818px;height:303px;background:var(--ink);border-bottom:3px solid var(--red)}
.section-title{color:var(--white);font-size:14.5px;font-weight:700}
.artist{width:140px;text-align:center;color:var(--white);font-size:12px;font-weight:600}
.artist-photo{width:128px;height:128px;border-radius:50%;margin:0 auto 12px;border:3px solid var(--white);box-shadow:3px 4px 8px rgba(0,0,0,.6)}
.artist-photo.active{border-color:var(--red)}
.slide-arrow{top:110px;width:20px;height:18px;fill:var(--white)}
.cta{left:340px;top:235px;width:137px;height:30px;background:linear-gradient(#f37a3e,#e85a26);color:var(--white);font-size:12px;display:flex;align-items:center;justify-content:center;gap:7px;border-radius:2px}

/* footer */
.site-footer{left:12px;top:926px;width:818px;height:156px;background:var(--footer)}
.col-title{color:var(--white);font-size:11.5px;font-weight:600;display:flex;align-items:center;gap:5px}
.col-title svg{width:11px;height:11px;fill:var(--red)}
.links{list-style:none;width:100px;font-size:9.5px}
.links li{padding:5px 0 5px 7px;border-bottom:1px solid var(--line);color:var(--white)}
.links li.active{color:var(--red);font-weight:600}
.tweet{font-size:8.5px;color:var(--white);line-height:12px}
.tweet a{color:var(--red);text-decoration:none}
.tweet small{display:block;margin-top:9px;font-size:7px}
.thumbs{display:grid;grid-template-columns:repeat(3,33px);gap:6px 7px}
.thumbs span{height:33px}
.email-field{width:136px;height:19px;background:#111;color:#555;font-size:7.5px;padding:5px}
.social{display:flex;gap:6px}
.social span{width:18px;height:18px;border-radius:3px}
.submit{width:58px;height:23px;background:var(--red);color:var(--white);font-size:11px;font-weight:700;display:flex;align-items:center;justify-content:center;border:1px solid #ff5a5a}

/* contact strip */
.contact-strip{left:12px;top:1082px;width:818px;height:66px;background:var(--ink-deep)}
.strip-name{left:0;top:9px;width:818px;color:var(--red);font-size:17px;letter-spacing:.5px}
.strip-info{left:0;top:38px;width:818px;display:flex;justify-content:center;align-items:center;gap:8px;color:var(--white);font-size:11.5px}
.strip-info svg{width:12px;height:13px;fill:var(--orange)}
.legal{left:12px;top:1148px;width:818px;height:33px;background:var(--ink);color:var(--white);font-size:7.5px}
</style>
</head>
<body>

<header class="site-header abs">
  <div class="brand abs"><span class="brand-mark"></span><span class="brand-name">Iron Heron</span></div>
  <nav class="nav abs">
    <a class="active" href="#"><svg viewBox="0 0 12 12"><path d="M6 1 0 6h2v5h3V8h2v3h3V6h2z"/></svg>HOME</a>
    <a href="#"><svg viewBox="0 0 14 12"><circle cx="4" cy="3" r="2"/><circle cx="10" cy="3" r="2"/><circle cx="7" cy="5" r="2.2"/><path d="M2 12c0-3 2-5 5-5s5 2 5 5z"/></svg>ARTISTS</a>
    <a href="#"><svg viewBox="0 0 14 12"><ellipse cx="5" cy="4.5" rx="5" ry="3.5"/><ellipse cx="9.5" cy="7" rx="4.5" ry="3.2"/></svg>CONTACT</a>
  </nav>
</header>

<section class="hero abs" role="img" aria-label="Close-up photograph of a hand playing a guitar fretboard">
  <svg class="hero-arrow abs" style="left:22px" viewBox="0 0 26 22"><path d="M0 11 11 0v7h15v8H11v7z"/></svg>
  <svg class="hero-arrow abs" style="right:17px" viewBox="0 0 26 22"><path d="M26 11 15 0v7H0v8h15v7z"/></svg>
  <h1 class="hero-title abs center">I LOVE SOUL/CLASSIC MUSIC</h1>
  <div class="hero-dots abs"><span class="on"></span><span></span><span></span></div>
</section>

<section class="player-band abs">
  <h2 class="player-title abs center">Our New Classic Out</h2>
  <div class="player-btns abs">
    <svg width="18" height="18" viewBox="0 0 18 18"><circle cx="9" cy="9" r="8" fill="none" stroke="#fff" stroke-width="1.3"/><path d="M9 6v6L5 9zm4 0v6L9 9z" fill="#fff"/></svg>
    <svg width="22" height="22" viewBox="0 0 22 22"><circle cx="11" cy="11" r="10" fill="none" stroke="#fff" stroke-width="1.5"/><path d="M8 6v10l8-5z" fill="#fff"/></svg>
    <svg width="18" height="18" viewBox="0 0 18 18"><circle cx="9" cy="9" r="8" fill="none" stroke="#fff" stroke-width="1.3"/><path d="M5 6v6l4-3zm4 0v6l4-3z" fill="#fff"/></svg>
  </div>
  <div class="player-bar abs">
    <span class="abs" style="left:10px;top:6px">00:02</span>
    <span class="abs" style="left:37px;top:10px;width:262px;height:2px;background:#ccc"></span>
    <span class="abs" style="left:37px;top:9px;width:44px;height:3px;background:var(--orange)"></span>
    <span class="abs" style="left:308px;top:6px">00:15</span>
    <div class="volume abs">
      <svg class="abs" style="left:9px;top:7px" width="8" height="8" viewBox="0 0 8 8"><path d="M0 2h2l3-2v8L2 6H0z" fill="#555"/></svg>
      <span class="abs" style="left:20px;top:10px;width:52px;height:2px;background:var(--orange)"></span>
      <svg class="abs" style="left:76px;top:7px" width="10" height="8" viewBox="0 0 10 8"><path d="M0 2h2l3-2v8L2 6H0z" fill="#555"/><path d="M6.5 2a3 3 0 0 1 0 4M8 1a5 5 0 0 1 0 6" stroke="#555" fill="none"/></svg>
    </div>
    <svg class="abs" style="left:443px;top:8px" width="7" height="6" viewBox="0 0 7 6"><path d="M0 0h7v1H0zm0 2.5h7v1H0zM0 5h7v1H0z" fill="#444"/></svg>
  </div>
</section>

<h2 class="intro-title abs center">Hello we’re <em>Iron Heron</em></h2>
<div class="intro-copy abs">
  <p>In elementum pellentesque dolor ac gravida. Pellentesque elit leo, accumsan sed consectetur a, semper ac sem. Morbi sodales bibendum risus nec laoreet. Mauris est nisi, consequat vitae porta et, hendrerit sed metus. Aliquam eu magna vel metus ultrices ornare in et nisi. Quisque porta sodales orci, eu auctor leo tincidunt nec. Suspendisse posuere blandit tortor sit amet varius. Integer condimentum rutrum mi quis lobortis. Etiam consectetur posuere pretium.</p>
  <p>Aliquam eu magna vel metus ultrices ornare in et nisi. Quisque porta sodales orci, eu auctor leo tincidunt nec. Suspendisse posuere blandit tortor sit amet varius. Integer condimentum rutrum mi quis lobortis. Etiam consectetur posuere pretium.</p>
</div>

<section class="artists abs">
  <h2 class="section-title abs center" style="left:0;top:13px;width:818px">Future Artists</h2>
  <svg class="slide-arrow abs" style="left:136px" viewBox="0 0 20 18"><path d="M0 9 9 0v6h11v6H9v6z"/></svg>
  <svg class="slide-arrow abs" style="left:663px" viewBox="0 0 20 18"><path d="M20 9 11 0v6H0v6h11v6z"/></svg>
  <div class="artist abs" style="left:164px;top:52px">
    <div class="artist-photo active" role="img" aria-label="Portrait photo of artist Aron Vale" style="background:radial-gradient(circle,#d9d9d9,#8a8a8a)"></div>Aron Vale</div>
  <div class="artist abs" style="left:339px;top:52px">
    <div class="artist-photo" role="img" aria-label="Photo of artist Tessa Noor singing on stage" style="background:radial-gradient(circle,#3c9fb0,#6b2a8e 70%,#2a1a3a)"></div>Tessa Noor</div>
  <div class="artist abs" style="left:515px;top:52px">
    <div class="artist-photo" role="img" aria-label="Photo of artist Milo Fenwick performing with a microphone" style="background:radial-gradient(circle,#8a3a7a,#3a1430)"></div>Milo Fenwick</div>
  <div class="cta abs"><svg width="18" height="14" viewBox="0 0 14 12" fill="#fff"><circle cx="4" cy="3" r="2"/><circle cx="10" cy="3" r="2"/><circle cx="7" cy="5" r="2.2"/><path d="M2 12c0-3 2-5 5-5s5 2 5 5z"/></svg>View All Artists</div>
</section>

<footer class="site-footer abs">
  <div class="abs" style="left:133px;top:32px">
    <h3 class="col-title"><svg viewBox="0 0 12 12"><path d="M4 0h4v3H7v2h4v3h1v4H8V8h1V6H3v2h1v4H0V8h1V5h4V3H4z"/></svg>Browse Around</h3>
    <ul class="links" style="margin-top:4px"><li class="active">Home</li><li>Artists</li><li>Contact</li></ul>
  </div>
  <div class="abs" style="left:268px;top:32px">
    <h3 class="col-title"><svg viewBox="0 0 12 12"><circle cx="6" cy="6" r="5"/></svg>Social Feed</h3>
    <p class="tweet" style="margin:10px 0 0 17px">resume template<br><a href="#">HTTP://ex.am/k7qpzt</a><small>July 01, 2014 07:56:37</small></p>
  </div>
  <div class="abs" style="left:403px;top:32px">
    <h3 class="col-title"><svg viewBox="0 0 12 12"><rect x="1" y="1" width="10" height="10" rx="2"/></svg>Photo Feed</h3>
    <div class="thumbs" role="img" aria-label="Grid of six music photo thumbnails" style="margin-top:7px">
      <span style="background:#777"></span><span style="background:#7a3a2a"></span><span style="background:#c0392b"></span>
      <span style="background:#555"></span><span style="background:#2a4a8a"></span><span style="background:#6a3a8a"></span>
    </div>
  </div>
  <div class="abs" style="left:548px;top:32px">
    <h3 class="col-title"><svg viewBox="0 0 12 10"><path d="M0 0h12v2L6 6 0 2zm0 3 6 4 6-4v7H0z"/></svg>Newsletter Signup</h3>
    <div class="email-field" style="margin-top:10px">Enter your email address</div>
    <div class="abs social" style="left:0;top:62px"><span style="background:#3b6fb0"></span><span style="background:#2aa6c8"></span><span style="background:#c0392b"></span></div>
    <div class="abs submit" style="left:78px;top:57px">Submit</div>
  </div>
</footer>

<section class="contact-strip abs">
  <h2 class="strip-name abs center" style="font-weight:400">IRON HERON</h2>
  <div class="strip-info abs">
    <svg viewBox="0 0 10 13"><path d="M5 0a5 5 0 0 0-5 5c0 4 5 8 5 8s5-4 5-8a5 5 0 0 0-5-5zm0 7a2 2 0 1 1 0-4 2 2 0 0 1 0 4z"/></svg>27 Larkmoor Lane, London, QX9 2ZZ
    <span>|</span>
    <svg viewBox="0 0 12 12"><path d="M2 0 4 0 5 3 3.5 4.5a7 7 0 0 0 4 4L9 7l3 1v2c0 1-1 2-2 2A10 10 0 0 1 0 2C0 1 1 0 2 0z"/></svg>0800.000.4417
    <span style="margin-left:6px">|</span>
    <svg viewBox="0 0 12 10"><path d="M0 0h12v2L6 6 0 2zm0 3 6 4 6-4v7H0z"/></svg>hello@iron-heron-example.com
  </div>
</section>

<div class="legal abs">
  <span class="abs" style="left:127px;top:13px">© Copyright 2014 Iron Heron. All rights reserved.</span>
  <span class="abs" style="left:568px;top:13px">Privacy Policy &nbsp;|&nbsp; Term &amp; Conditions</span>
</div>

</body>
</html>
```